Startup Drone Platform Company business card

We are needing a business card design for our employees. We are a startup drone platform. We are looking for a business card that has our logo on one side, with the employee/company details on the opposite side. We are looking for something that is very eye catching, modern, and bold.

Target Market(s)

This will target both drone pilots and drone businesses, along with all the industries that could utilize drone services (aerial video, aerial photos, inspections, 3d mapping, etc).

Industry/Entity Type

Business

```html
<!DOCTYPE html>
<html lang="en">
<head>
<meta charset="UTF-8">
<title>Skyward Lift Business Card</title>
<link href="https://fonts.googleapis.com/css2?family=Montserrat:wght@400;700&display=swap" rel="stylesheet">
<style>
  :root {
    --page: #e9e9e7;
    --ink-dark: #232323;
    --ink-text: #111111;
    --teal: #3bb9c6;
    --grey-text: #7a7a7a;
    --rule: #b5b5b5;
    --white: #ffffff;
  }
  * { margin: 0; padding: 0; box-sizing: border-box; }
  html, body {
    width: 1200px; height: 1000px; overflow: hidden;
    background: var(--page);
    font-family: "Montserrat", sans-serif;
  }
  .card {
    position: absolute; left: 250px;
    width: 700px; height: 400px;
    box-shadow: 0 6px 18px rgba(0,0,0,0.18);
    overflow: hidden;
  }
  /* Back side */
  .card-back { top: 50px; background: var(--ink-dark); }
  .back-brand {
    position: absolute; left: 0; right: 0; top: 150px;
    display: flex; justify-content: center; align-items: center; gap: 18px;
  }
  .brand-dot {
    width: 34px; height: 34px; border-radius: 50%;
    border: 4px solid var(--teal);
  }
  .back-brand-name {
    color: var(--white); font-weight: 400; font-size: 36px; letter-spacing: 10px;
  }
  .back-url {
    position: absolute; left: 0; right: 0; top: 320px;
    text-align: center; color: #cfcfcf; font-size: 16px; letter-spacing: 1px;
  }
  .back-url .accent { color: var(--teal); }

  /* Front side */
  .card-front { top: 520px; background: var(--white); }
  .front-brand {
    position: absolute; right: 45px; top: 58px;
    display: flex; align-items: center; gap: 16px;
    color: var(--ink-text); font-size: 24px; letter-spacing: 9px;
  }
  .front-brand .brand-dot { width: 22px; height: 22px; border-width: 3px; }
  .holder { position: absolute; left: 60px; top: 130px; }
  .holder-name { color: var(--teal); font-weight: 700; font-size: 24px; }
  .holder-role { color: var(--grey-text); font-size: 17px; margin-top: 2px; }
  .divider {
    position: absolute; left: 60px; right: 90px; top: 205px;
    height: 1px; background: var(--rule);
  }
  .contacts { position: absolute; left: 60px; top: 222px; list-style: none; }
  .contacts li {
    display: flex; align-items: center; gap: 8px;
    color: var(--grey-text); font-size: 17px; line-height: 27px;
  }
  .contacts svg { width: 15px; height: 15px; fill: var(--teal); }
  .address {
    position: absolute; right: 90px; top: 280px; text-align: right;
    color: var(--grey-text); font-size: 18px; line-height: 26px;
  }
  .band-dark {
    position: absolute; left: 0; bottom: 30px; width: 330px; height: 18px;
    background: var(--ink-dark);
  }
  .band-teal {
    position: absolute; right: 0; bottom: 0; width: 400px; height: 44px;
    background: var(--teal);
    clip-path: polygon(30px 0, 100% 0, 100% 100%, 0 100%);
  }
</style>
</head>
<body>
  <section class="card card-back">
    <div class="back-brand">
      <span class="brand-dot"></span>
      <span class="back-brand-name">SKYWARD LIFT</span>
    </div>
    <p class="back-url">www.<span class="accent">skywardlift</span>.com</p>
  </section>

  <section class="card card-front">
    <div class="front-brand">
      <span>SKYWARD</span>
      <span class="brand-dot"></span>
      <span>LIFT</span>
    </div>
    <div class="holder">
      <p class="holder-name">Owen Harper</p>
      <p class="holder-role">Founder &amp; CEO</p>
    </div>
    <div class="divider"></div>
    <ul class="contacts">
      <li>
        <svg viewBox="0 0 16 16" aria-hidden="true"><path d="M3 2h3l1.5 3.5-2 1.3a8 8 0 0 0 3.7 3.7l1.3-2L14 10v3a1 1 0 0 1-1 1A11 11 0 0 1 2 3a1 1 0 0 1 1-1z"/></svg>
        014-555-0192
      </li>
      <li>
        <svg viewBox="0 0 16 16" aria-hidden="true"><path d="M1 3h14v10H1z M1.5 3.5 8 9l6.5-5.5" stroke="#fff" stroke-width="1"/></svg>
        hello@skywardlift.com
      </li>
      <li>
        <svg viewBox="0 0 16 16" aria-hidden="true"><circle cx="8" cy="8" r="7"/><path d="M1 8h14M8 1c3 3.5 3 10.5 0 14M8 1c-3 3.5-3 10.5 0 14" stroke="#fff" stroke-width="1" fill="none"/></svg>
        www.skywardlift.com
      </li>
    </ul>
    <p class="address">Street name, Suite 100<br>State, Zip Code, Country</p>
    <div class="band-dark"></div>
    <div class="band-teal"></div>
  </section>
</body>
</html>
```